Flyer für kleine christliche Gemeinde
professionelles Vorgehen. pulvrin hat sehr gut Sinn und Konzept unserer Veranstaltung erfasst und den Flyer mit passenden Bildern und angemessener Designgestaltung versehen. Stach aus den anderen Vorschlägen heraus. Änderungswünsche und auch Planänderungen unsererseits wurden geduldig und sehr geschmackvoll umgesetzt. Wer ein fundiertes, modernes und ansprechendes, passendes Design braucht ist mit diesem Designer gut beraten.
Zielgruppe
kleine christliche Gemeinde, Einladung zu einer Vortragsreihe zu aktuellen Themen /Krisen unserer Zeit, Zielgruppe: Erwachse Menschen aller Couleur mit Interesse an aktuellem Zeitgeschehen und Antworten für die Probleme unserer Zeit, Sinn- und Orientierungssuchende, Bibelinteressierte
Aufgabenstellung
Aufmerksamkeit fesselnder, dennoch seriös wirkender, informativer Flyer als Einladung zu einer Vortragsreihe, Verteilung per Hand auf der Straße und in Briefkästen, Information zum Redner kürzen wenn nötig, Anfahrtsskizze und Informationen zu Erreichbarkeit (Bus...), Stockbilder möglichst kostenfreie verwenden,

```html
<!DOCTYPE html>
<html lang="de">
<head>
<meta charset="utf-8">
<title>Signale unserer Zeit – Flyer</title>
<link rel="stylesheet" href="https://fonts.googleapis.com/css2?family=Domine:wght@400;700&family=Noto+Serif:ital,wght@0,400;0,700;1,400&family=Open+Sans:ital,wght@1,400&display=swap">
<style>
:root{
  --bg:#e6e4e1;
  --paper:#ffffff;
  --ink:#333333;
  --purple:#7b72b0;
  --purple-text:#7b6fb5;
  --green:#6b9a48;
  --red:#a52a1f;
  --white:#ffffff;
}
*{margin:0;padding:0;box-sizing:border-box}
html,body{width:1200px;height:1200px;overflow:hidden;background:var(--bg)}
.stage{position:relative;width:1200px;height:1200px;overflow:hidden;background:var(--bg);font-family:"Noto Serif",serif;color:var(--ink)}
.panel{position:absolute;background:var(--paper);overflow:hidden;box-shadow:0 2px 8px rgba(0,0,0,.18)}

/* cover */
.cover{left:300px;top:45px;width:280px;height:555px;background:#222}
.cover-photo{position:absolute;inset:0;background:radial-gradient(ellipse at 50% 62%,#8a8a8a 0%,#4a4a4a 35%,#1e1e1e 75%),#222}
.cover-photo::after{content:"";position:absolute;inset:0;background:linear-gradient(180deg,rgba(0,0,0,.35) 0%,rgba(0,0,0,0) 40%,rgba(0,0,0,.55) 100%)}
.cover-title{position:absolute;left:0;top:0;width:100%;color:var(--white);font-family:"Domine",serif;font-weight:700;line-height:1}
.t-signale{position:absolute;left:38px;top:42px;font-size:52px;letter-spacing:.5px}
.t-unserer{position:absolute;right:42px;top:100px;font-size:28px}
.t-zeit{position:absolute;left:38px;top:134px;font-size:58px}
.t-weg{position:absolute;left:172px;top:148px;font-size:14px;font-weight:400;line-height:1.3}
.t-echter{position:absolute;left:70px;top:198px;font-size:14px;font-weight:400}
.cover-series{position:absolute;left:0;right:20px;top:420px;text-align:center;color:var(--white);font-family:"Domine",serif;font-weight:700;font-size:19px;line-height:1.2}
.cover-date{position:absolute;left:0;right:60px;top:478px;text-align:center;color:var(--white);font-family:"Domine",serif;font-weight:700;font-size:15px;line-height:1.3}
.cover-badge{position:absolute;right:-40px;bottom:-40px;width:130px;height:130px;border-radius:50%;background:var(--purple)}
.cover-badge span{position:absolute;left:28px;top:34px;color:var(--white);font-family:"Domine",serif;font-weight:700;font-size:12px;line-height:1.1;text-align:center}

/* location panel */
.location{left:610px;top:45px;width:274px;height:555px}
.loc-head{position:absolute;left:48px;top:26px;color:var(--purple-text);font-family:"Domine",serif;font-weight:700;font-size:9px}
.loc-list{position:absolute;left:24px;top:50px;width:230px;list-style:none}
.loc-list li{position:relative;padding-left:24px;font-family:"Domine",serif;font-size:8px;line-height:1.4;margin-bottom:9px}
.loc-num{position:absolute;left:0;top:-1px;width:15px;height:15px;border-radius:50%;background:var(--red);color:var(--white);font-size:9px;line-height:15px;text-align:center}
.hotel-name{display:block;color:var(--red);font-family:"Domine",serif;font-size:11px;margin-bottom:6px}
.hotel-addr{font-size:9px}
.map{position:absolute;left:17px;top:196px;width:241px;height:318px;background:linear-gradient(160deg,#f2f2f2 0%,#e7e7e9 55%,#dcdde0 100%)}
.map-credit{position:absolute;right:16px;top:517px;font-size:5.5px;font-family:"Domine",serif}

/* inside spread */
.spread{left:323px;top:624px;width:554px;height:555px}
.intro{position:absolute;left:18px;top:22px;width:244px;font-size:8.7px;line-height:1.5;text-align:justify}
.quote{position:absolute;left:38px;top:204px;width:215px;color:var(--red);font-family:"Open Sans",sans-serif;font-style:italic;font-size:8.6px;line-height:1.43}
.quote-mark{position:absolute;font-family:"Domine",serif;font-weight:700;font-size:46px;line-height:1;color:var(--red)}
.quote-open{left:-5px;top:-6px}
.quote-close{right:-2px;bottom:-24px}
.quote p{text-indent:30px}
.source{position:absolute;right:290px;top:308px;font-size:5.6px}
.questions{position:absolute;left:16px;top:326px;display:flex;gap:6px}
.question{width:76px;height:76px;display:flex;align-items:center;justify-content:center;text-align:center;color:var(--white);font-family:"Domine",serif;font-size:8.5px;line-height:1.4;padding:4px}
.q-purple{background:var(--purple)}
.q-green{background:var(--green)}
.closing{position:absolute;left:18px;top:420px;width:142px;font-size:8.7px;line-height:1.5;text-align:justify}
.photo{position:absolute}
.photo-statue{left:182px;top:422px;width:76px;height:76px;background:linear-gradient(180deg,#b7cde0 0%,#9aa7b4 60%,#6b6660 100%)}
.photo-hands{left:277px;top:0;width:136px;height:137px;background:radial-gradient(circle at 50% 45%,#7a6a5e 0%,#2a2624 55%,#111 100%)}
.photo-silhouette{left:420px;top:0;width:134px;height:137px;background:radial-gradient(circle at 50% 40%,#8fb0e0 0%,#3f63b0 55%,#1c2e70 100%)}
.photo-woman{left:420px;top:143px;width:134px;height:137px;background:radial-gradient(circle at 50% 45%,#a88f7a 0%,#5a4a3a 55%,#3a2f25 100%)}
.program{position:absolute;left:277px;top:143px;width:136px;height:137px;background:var(--green);list-style:none;padding:8px 6px 0 8px}
.program li{display:flex;gap:6px;margin-bottom:6px;color:var(--white)}
.prog-num{font-family:"Domine",serif;font-size:22px;line-height:1;width:18px;flex:none}
.prog-title{font-family:"Domine",serif;font-weight:700;font-size:8.6px;line-height:1.05}
.prog-time{display:block;font-family:"Domine",serif;font-weight:400;font-size:6px;margin-top:1px}
.speaker{position:absolute;left:277px;top:289px;width:277px;height:266px;background:var(--purple);color:var(--white)}
.photo-speaker{left:14px;top:14px;width:98px;height:103px;background:linear-gradient(180deg,#3b6fb0 0%,#2a4f86 60%,#1d2a44 100%)}
.speaker-caption{position:absolute;left:14px;top:121px;font-size:5.8px}
.speaker-text{position:absolute;left:14px;top:12px;width:250px;font-size:7.7px;line-height:1.52;text-align:justify}
.speaker-text::before{content:"";float:left;width:104px;height:118px}
.speaker-text strong{font-family:"Domine",serif}
</style>
</head>
<body>
<div class="stage">

  <section class="panel cover">
    <div class="cover-photo" role="img" aria-label="Schwarzweißfoto eines älteren Mannes mit Mütze vor einem Kreuz im Gegenlicht"></div>
    <h1 class="cover-title">
      <span class="t-signale">Signale</span>
      <span class="t-unserer">unserer</span>
      <span class="t-zeit">Zeit</span>
      <span class="t-weg">Und der<br>Weg zu</span>
      <span class="t-echter">echter Unabhängigkeit</span>
    </h1>
    <p class="cover-series">Eine Kurz-Serie mit<br>Daniel Moreno</p>
    <p class="cover-date">Pfingsten,<br>18-20. Mai 2024</p>
    <div class="cover-badge"><span>Eintritt<br>frei</span></div>
  </section>

  <section class="panel location">
    <h2 class="loc-head">Veranstaltungsort:</h2>
    <ol class="loc-list">
      <li><span class="loc-num">1</span><span class="hotel-name">Stadthotel Lindenfeld</span><span class="hotel-addr">Lindenallee 23 in 16500 Lindenfeld<br>Im großen Tagungsraum</span></li>
      <li><span class="loc-num">2</span>15 Gehminuten vom Bahnhof Lindenfeld</li>
      <li><span class="loc-num">3</span>4 min mit dem Bus 804 oder 821 vom Bahnhof Lindenfeld</li>
      <li><span class="loc-num">4</span>Kostenlose Parkplätze direkt am Hotel oder auf dem Marktparkplatz</li>
    </ol>
    <div class="map" role="img" aria-label="Anfahrtskarte vom Bahnhof zum Hotel mit markierten Punkten 1 bis 4"></div>
    <p class="map-credit">Kartendaten © 2024 Kartenwerk Nord</p>
  </section>

  <section class="panel spread">
    <p class="intro">Fakenews im Netz, Verschwörungstheorien, aufsehenerregende Berichterstattung und voreilige politische Planspiele verunsichern die Menschen. Politiker und die Mächtigen der Welt suchen in Weltwirtschaftsforen und Klimakonferenzen nach Antworten und Lösungswegen globaler Probleme. Wirtschaft, Wissenschaft, Politik und Kirchen suchen nach Orientierung und Führung, geradezu nach einem Erlöser, der die Kräfte für den Rettungsweg unseres Planeten eint. Die tatsächliche Ratlosigkeit der Großen und Mächtigen und die Verunsicherung der Bevölkerung der Welt spiegeln sich dramatisch in folgenden Worten wieder:</p>

    <blockquote class="quote">
      <span class="quote-mark quote-open">“</span>
      <p>Und es werden Zeichen geschehen an Sonne und Mond und Sternen, und auf Erden Angst der Völker vor Ratlosigkeit bei dem Tosen des Meeres und der Wogen, da die Menschen in Ohnmacht sinken werden vor Furcht und Erwartung dessen, was über den Erdkreis kommen soll; denn die Kräfte des Himmels werden erschüttert werden.</p>
      <span class="quote-mark quote-close">”</span>
    </blockquote>
    <p class="source">Die Bibel, Lukas Kapitel 21, Vers 25-26</p>

    <div class="questions">
      <div class="question q-purple">Doch wo stehen wir?</div>
      <div class="question q-green">Wie kommen wir durch die Wirrnisse dieser Zeit?</div>
      <div class="question q-purple">Welche echten Lösungsansätze gibt es?</div>
    </div>

    <p class="closing">Erfahren Sie Gottes Fahrplan für diese Welt. Lernen Sie den einzigen Ausweg und die Chance kennen, Ihre persönliche Individualität und einen kühlen Kopf zu bewahren. Finden Sie echte Sicherheit auf ihrem Weg in unsicheren Zeiten.</p>
    <div class="photo photo-statue" role="img" aria-label="Steinstatue einer verhüllten Figur vor hellem Himmel"></div>

    <div class="photo photo-hands" role="img" aria-label="Gefaltete Hände vor dunklem Hintergrund"></div>
    <div class="photo photo-silhouette" role="img" aria-label="Silhouette einer sitzenden Person in blauem Licht"></div>

    <ol class="program">
      <li><span class="prog-num">1.</span><span class="prog-title">Ein sicherer Anker in ungewisser Zeit<span class="prog-time">Sa., 18.5., 18:00 Uhr</span></span></li>
      <li><span class="prog-num">2.</span><span class="prog-title">Systeme der Macht -der Kampf um unseren Verstand<span class="prog-time">Sa., 19.5., 18:00 Uhr</span></span></li>
      <li><span class="prog-num">3.</span><span class="prog-title">Erzwungene Loyalität -wie wir sie zeigen müssen<span class="prog-time">So., 20.5., 18:00 Uhr</span></span></li>
    </ol>
    <div class="photo photo-woman" role="img" aria-label="Nachdenkliche Frau im grünen Pullover"></div>

    <div class="speaker">
      <div class="photo photo-speaker" role="img" aria-label="Porträt des Redners im Anzug"></div>
      <p class="speaker-caption">Pr. Daniel Moreno</p>
      <p class="speaker-text"><strong>Zum Sprecher:</strong><br>Pastor Daniel Moreno wurde in Santiago, Dominikanische Republik, geboren. Er ist Pastor der Living Hope Church, Herausgeber des Hope Herald und moderiert wöchentliche Radiosendungen. Seit über 20 Jahren führt er eine landesweite Kampagne zum Verständnis der biblischen Weissagungen sowohl in den Vereinigten Staaten als auch im Ausland durch. Pastor Moreno kombiniert ein tiefgründiges Verständnis der Weltgeschichte, politischer und religiöser Zusammenhänge mit den faszinierenden Fakten der weitreichenden Prophezeiungen in der Bibel. Im Zusammenspiel mit seiner lateinamerikanischen Begeisterung gibt er den Zuhörern spannende und verständige Einblicke in die dramatischen Entwicklungen unserer Gesellschaft und Zukunftsperspektiven.</p>
    </div>
  </section>

</div>
</body>
</html>
```